KRM

I just wrote a novel that I plan on marketing through my website. Please use my uploaded files to add on to your design... The name of the book is "Lanterns under the frost".

Industry/Entity Type

Marketing

Font styles to use
Serif
Sans Serif

Colors

Designer to choose colors to be used in the design.

```html
<!DOCTYPE html>
<html lang="en">
<head>
<meta charset="utf-8">
<title>Lanterns under the frost</title>
<link rel="stylesheet" href="https://fonts.googleapis.com/css2?family=Anton&family=Creepster&family=Fjalla+One&family=Open+Sans:wght@400;600;700&family=Roboto:wght@300;400&display=swap">
<style>
:root{
  --page-dark:#1b1b1b;
  --page-mid:#2a2a2a;
  --navy:#221c6e;
  --black:#000;
  --white:#fff;
  --blood:#b31b1b;
  --band-red:#7f1010;
  --grey-panel:#ebebeb;
  --icon-dark:#222;
  --heading-grey:#444;
  --copy-grey:#666;
  --gold:#ffd400;
}
*{box-sizing:border-box;margin:0;padding:0}
html,body{width:1200px;height:1177px;overflow:hidden}
body{background:linear-gradient(90deg,var(--page-dark),var(--page-mid) 50%,var(--page-dark));font-family:Arial,Helvetica,sans-serif;position:relative}
.site{position:absolute;left:110px;top:0;width:980px;height:1177px;background:var(--white)}
.abs{position:absolute}

.header{left:0;top:0;width:980px;height:137px;background:var(--white)}
.brand{left:36px;top:14px;display:flex;align-items:center;gap:10px}
.brand-dot{width:34px;height:34px;border-radius:50%;background:var(--black)}
.brand-name{font-family:'Anton',sans-serif;font-size:52px;color:var(--black);line-height:110px}
.title{left:212px;top:30px;white-space:nowrap;line-height:80px}
.title-lead{font-family:'Creepster',cursive;font-size:66px;color:var(--blood);margin-right:14px}
.title-rest{font-family:'Anton',sans-serif;font-size:56px;color:var(--black);letter-spacing:.5px}

.rule{left:0;top:137px;width:980px;height:5px;background:var(--black)}
.nav{left:0;top:142px;width:980px;height:47px;background:var(--navy);display:flex}
.nav a{font-family:'Fjalla One',sans-serif;font-size:19px;color:var(--white);text-decoration:none;line-height:49px;text-transform:uppercase}
.nav .active{background:var(--black);width:124px;text-align:center}
.nav .item{margin-left:39px;margin-right:39px}

.hero{left:0;top:189px;width:980px;height:338px;background:#555}
.tile{position:absolute}
.hero-band{left:0;top:527px;width:980px;height:10px;background:var(--band-red)}
.book{left:62px;top:258px;width:195px;height:335px;background:linear-gradient(180deg,#2a247a,#1e1a66);box-shadow:4px 6px 10px rgba(0,0,0,.5);transform:rotate(-2deg)}
.book-band{position:absolute;left:0;top:140px;width:100%;height:90px;background:linear-gradient(180deg,#8a1414,#3a0e2e)}

.price-wrap{left:285px;top:493px;width:668px;height:110px;background:var(--white)}
.price{left:304px;top:510px;width:627px;height:73px;background:var(--black);color:var(--white);font-family:'Roboto',sans-serif;font-weight:300;font-size:41px;line-height:73px;text-align:right;padding-right:18px}
.price b{font-weight:400}

.pitch{left:74px;top:625px;width:860px}
.pitch h2{font-weight:400;font-size:23px;color:#333}
.pitch h2 span{color:var(--blood)}
.pitch p{font-size:13.5px;color:#333;line-height:17px;margin-top:1px}

.themes{left:0;top:742px;width:980px;height:282px;background:var(--grey-panel)}
.theme{position:absolute;top:55px;width:210px;font-family:'Open Sans',sans-serif}
.theme-icon{width:79px;height:79px;border-radius:50%;background:var(--icon-dark);margin:0 auto;display:flex;align-items:center;justify-content:center}
.theme h3{text-align:center;font-size:18px;font-weight:600;color:var(--heading-grey);margin-top:13px}
.theme p{font-size:13px;line-height:15.5px;color:var(--copy-grey);margin-top:6px}

.order{left:0;top:1024px;width:980px;height:114px;background:var(--navy);font-family:'Open Sans',sans-serif}
.order h2{position:absolute;left:34px;top:18px;font-size:29px;font-weight:700;color:var(--gold)}
.order .or{position:absolute;left:36px;top:58px;font-size:30px;color:var(--gold)}
.order .links{position:absolute;left:101px;top:66px;font-family:Arial,sans-serif;font-size:12px;line-height:14px;color:var(--gold)}
.order .mail{position:absolute;left:337px;top:66px;font-family:Arial,sans-serif;font-size:12px;color:var(--gold)}
.contact{position:absolute;left:635px;top:16px;width:319px;height:85px;background:var(--black);text-align:center;color:var(--blood)}
.contact .who{font-size:23px;line-height:26px;margin-top:8px}
.contact .phone{font-size:45px;font-weight:700;line-height:50px}

.payments{left:0;top:1138px;width:980px;height:39px;background:var(--band-red);color:#e4dada;font-size:14px;text-align:center;line-height:37px}
</style>
</head>
<body>
<div class="site">
  <header class="abs header">
    <div class="abs brand"><span class="brand-dot"></span><span class="brand-name">KRM</span></div>
    <h1 class="abs title"><span class="title-lead">LANTERNS</span><span class="title-rest">UNDER THE FROST</span></h1>
  </header>
  <div class="abs rule"></div>
  <nav class="abs nav">
    <a class="active" href="#">Home</a>
    <a class="item" href="#">About the book</a>
    <a class="item" href="#">Book features</a>
    <a class="item" href="#">Author</a>
    <a class="item" href="#">Contact us</a>
  </nav>

  <div class="abs hero" role="img" aria-label="Collage of city scenes: stacked cash, a group of friends, a police car, the author, a bedroom scene and handguns">
    <div class="tile" style="left:0;top:0;width:308px;height:156px;background:linear-gradient(135deg,#8c8a7a,#5e5a4c)"></div>
    <div class="tile" style="left:0;top:156px;width:256px;height:182px;background:linear-gradient(135deg,#a4584a,#d9d6cf)"></div>
    <div class="tile" style="left:256px;top:156px;width:174px;height:182px;background:linear-gradient(135deg,#d79a5e,#8c4a2a)"></div>
    <div class="tile" style="left:310px;top:0;width:324px;height:338px;background:linear-gradient(180deg,#c8cfc4,#4a4e52 60%,#7a6c6a)"></div>
    <div class="tile" style="left:635px;top:0;width:345px;height:155px;background:linear-gradient(135deg,#6a6c6e,#2e3236)"></div>
    <div class="tile" style="left:635px;top:156px;width:180px;height:182px;background:linear-gradient(135deg,#4a4448,#b04a8a 70%,#3a3034)"></div>
    <div class="tile" style="left:815px;top:156px;width:165px;height:182px;background:linear-gradient(135deg,#c8a032,#2a2a2a 60%,#b89030)"></div>
  </div>
  <div class="abs hero-band"></div>
  <div class="abs book" role="img" aria-label="Book cover of Lanterns under the frost"><div class="book-band"></div></div>

  <div class="abs price-wrap"></div>
  <div class="abs price">At <b>$14.99</b> you can own your copy.</div>

  <section class="abs pitch">
    <h2>A story of <span>Money, Murder, Sex and family</span> ties in the heart of the city.</h2>
    <p>Ready along as Marcus T. Hale masterfully paint this Harlow Bay tale like no other ~ The "Ridge boys" clash in a rain of bullets against North sides own "Dock boys."</p>
  </section>

  <section class="abs themes">
    <div class="theme" style="left:34px">
      <div class="theme-icon"><svg width="44" height="44" viewBox="0 0 44 44" fill="none" stroke="#fff" stroke-width="3"><circle cx="15" cy="27" r="10"/><circle cx="30" cy="20" r="9"/><text x="15" y="32" font-size="13" font-family="Arial" fill="#fff" stroke="none" text-anchor="middle" font-weight="700">$</text><text x="30" y="25" font-size="12" font-family="Arial" fill="#fff" stroke="none" text-anchor="middle" font-weight="700">$</text></svg></div>
      <h3>money</h3>
      <p>Ut enim ad minim veniaxam, quis nostrud exercittion ullamco laboris nisi ut aliquip ex ea commodo consequat.</p>
    </div>
    <div class="theme" style="left:268px">
      <div class="theme-icon"><svg width="44" height="44" viewBox="0 0 44 44" fill="none" stroke="#fff" stroke-width="3"><circle cx="22" cy="22" r="11"/><path d="M22 6v10M22 28v10M6 22h10M28 22h10"/></svg></div>
      <h3>murder</h3>
      <p>Duis aute irure dolor in reprehderit in volptate velit esse cillm dolore eu fugiat nulla paiatur. Excepteur sint occaecat cupidatatnon proident.</p>
    </div>
    <div class="theme" style="left:509px">
      <div class="theme-icon"><svg width="44" height="44" viewBox="0 0 44 44" fill="none" stroke="#fff" stroke-width="3.5"><circle cx="17" cy="22" r="8"/><circle cx="26" cy="18" r="8"/><path d="M17 30v10M12 35h10M32 12l7-7M33 5h6v6"/></svg></div>
      <h3>sex</h3>
      <p>Ut enim ad minim veniaxam, quis nostrud exercittion ullamco laboris nisi ut aliquip ex ea commodo consequat.</p>
    </div>
    <div class="theme" style="left:748px">
      <div class="theme-icon"><svg width="44" height="44" viewBox="0 0 44 44" fill="#fff"><circle cx="11" cy="17" r="4"/><circle cx="22" cy="15" r="5"/><circle cx="33" cy="17" r="4"/><path d="M4 30q0-8 7-8t7 8zM14 31q0-10 8-10t8 10zM26 30q0-8 7-8t7 8z"/></svg></div>
      <h3>family</h3>
      <p>Duis aute irure dolor in reprehderit in volptate velit esse cillm dolore eu fugiat nulla paiatur. Excepteur sint occaecat cupidatatnon proident.</p>
    </div>
  </section>

  <section class="abs order">
    <h2>TO PURCHASE YOUR ORDER BACK COPY</h2>
    <span class="or">or</span>
    <div class="links">www.krmpublishing.example<br>www.lanternsunderthefrost.example</div>
    <div class="mail">email: lanternsfrost24@example.com</div>
    <div class="contact"><div class="who">Contact Marc Hale @</div><div class="phone">555-014-2290</div></div>
  </section>
  <footer class="abs payments">We accept all major credit and debit cards for those individuals who wish to order on-line!</footer>
</div>
</body>
</html>
```